Quiet Harbor Podcast Business Card Design

Needing a business card with the logo design provided for Quiet Harbor Podcast. I am looking for a modern style that fits the current logo.

Info:
Name: Teodor Vask
Title: Creator/Host
Email: teodor@quietharborcast.com
Phone: (555) 274-9163
www.quietharborcast.com
Twitter: @qharborcast
Instagram: @quietharborcastshow
Facebook: Quiet Harbor Podcast

Industry/Entity Type

Business

Font styles to use
Sans Serif

Colors
000000
ffffff

Requirements
Must have
• modern, clean design
Nice to have
• social media contact info

```html
<!DOCTYPE html>
<html lang="en">
<head>
<meta charset="utf-8">
<title>Quiet Harbor Podcast — Business Card</title>
<link rel="stylesheet" href="https://fonts.googleapis.com/css2?family=Montserrat:wght@400;600&family=Roboto+Condensed:wght@400&display=swap">
<style>
  :root {
    --page-bg: #d9d9d9;
    --card-black: #231f20;
    --panel-dark: #2b2a2c;
    --ink-white: #ffffff;
    --rule-grey: #bdbdbd;
  }
  * { box-sizing: border-box; margin: 0; padding: 0; }
  html, body { width: 1200px; height: 1200px; overflow: hidden; }
  body {
    background: var(--page-bg);
    display: flex;
    flex-direction: column;
    align-items: center;
    justify-content: center;
    gap: 44px;
  }
  .card {
    position: relative;
    width: 900px;
    height: 514px;
    background: var(--card-black);
    color: var(--ink-white);
    overflow: hidden;
  }

  /* Front */
  .card-front {
    display: flex;
    flex-direction: column;
    align-items: center;
    justify-content: center;
  }
  .brand-name {
    font-family: "Montserrat", sans-serif;
    font-weight: 600;
    font-size: 54px;
    letter-spacing: 2px;
    text-transform: uppercase;
  }
  .brand-tag {
    margin-top: 10px;
    font-family: "Montserrat", sans-serif;
    font-weight: 400;
    font-size: 16px;
    letter-spacing: 14px;
    padding-left: 14px;
    text-transform: uppercase;
  }

  /* Back */
  .contact-block {
    position: absolute;
    left: 60px;
    top: 80px;
    width: 440px;
  }
  .person-name {
    font-family: "Montserrat", sans-serif;
    font-weight: 400;
    font-size: 42px;
    letter-spacing: 1px;
    text-transform: uppercase;
    line-height: 1;
  }
  .person-title {
    margin-top: 14px;
    font-family: "Roboto Condensed", sans-serif;
    font-size: 28px;
  }
  .divider {
    margin: 20px 0 34px -10px;
    width: 470px;
    border: 0;
    border-top: 1px solid var(--rule-grey);
  }
  .contact-list {
    list-style: none;
    font-family: "Roboto Condensed", sans-serif;
    font-size: 28px;
    line-height: 1;
  }
  .contact-list li {
    display: flex;
    align-items: center;
    gap: 12px;
    height: 42px;
  }
  .contact-list + .contact-list { margin-top: 30px; }
  .social-mark {
    width: 26px;
    height: 26px;
    border-radius: 5px;
    background: var(--ink-white);
    flex: none;
  }
  .contact-icon {
    width: 26px;
    height: 26px;
    flex: none;
  }
  .logo-panel {
    position: absolute;
    left: 520px;
    top: 0;
    width: 320px;
    height: 370px;
    background: var(--panel-dark);
    border-radius: 0 0 44px 44px;
    display: flex;
    align-items: center;
    justify-content: center;
    text-align: center;
  }
  .panel-name {
    font-family: "Montserrat", sans-serif;
    font-weight: 600;
    font-size: 52px;
    line-height: 1.1;
    letter-spacing: 2px;
    text-transform: uppercase;
  }
</style>
</head>
<body>

  <section class="card card-front" aria-label="Card front">
    <div class="brand-name">Quiet Harbor</div>
    <div class="brand-tag">Podcast</div>
  </section>

  <section class="card card-back" aria-label="Card back">
    <div class="contact-block">
      <h1 class="person-name">Teodor Vask</h1>
      <p class="person-title">Creator/ Host</p>
      <hr class="divider">
      <ul class="contact-list social-list">
        <li><span class="social-mark"></span>@qharborcast</li>
        <li><span class="social-mark"></span>Quiet Harbor Podcast</li>
        <li><span class="social-mark"></span>@quietharborcastshow</li>
      </ul>
      <ul class="contact-list direct-list">
        <li>
          <svg class="contact-icon" viewBox="0 0 26 26" aria-hidden="true">
            <rect width="26" height="26" rx="4" fill="#fff"/>
            <path d="M5 11c0-3 4-4 8-4s8 1 8 4l-3 1-1-2h-8l-1 2z" fill="#231f20"/>
            <rect x="7" y="13" width="12" height="7" rx="1.5" fill="#231f20"/>
          </svg>
          (555) 274-9163
        </li>
        <li>
          <svg class="contact-icon" viewBox="0 0 26 26" aria-hidden="true">
            <rect width="26" height="26" rx="4" fill="#fff"/>
            <g fill="none" stroke="#231f20" stroke-width="1.5">
              <circle cx="13" cy="13" r="8"/>
              <ellipse cx="13" cy="13" rx="3.5" ry="8"/>
              <line x1="5" y1="13" x2="21" y2="13"/>
            </g>
          </svg>
          www.quietharborcast.com
        </li>
        <li>
          <svg class="contact-icon" viewBox="0 0 26 26" aria-hidden="true">
            <rect width="26" height="26" rx="4" fill="#fff"/>
            <g fill="none" stroke="#231f20" stroke-width="1.5">
              <rect x="5" y="8" width="16" height="11"/>
              <polyline points="5,8 13,14 21,8"/>
            </g>
          </svg>
          teodor@quietharborcast.com
        </li>
      </ul>
    </div>
    <div class="logo-panel">
      <div class="panel-name">Quiet<br>Harbor</div>
    </div>
  </section>

</body>
</html>
```